business card

Business card for new business.
Red and black corporate colors.
Card can have an Indsutrial feel to it. Feel free to add Rust, Bolted steel, or graphics as you see fit. We provide highly specialized services to the below mentioned industries.
Keep information out of corners so that if I want I can choose rounded corners.
Information
- front. name - title - phone - email
- Rear
Pipeline - Ports - Heavy Civil Works - Forestry - Power
Ashford - Brookvale - Port Redmond - Kestrel Ridge - Lakemont

```html
<!DOCTYPE html>
<html lang="en">
<head>
<meta charset="utf-8">
<title>Girderline Business Card</title>
<link rel="stylesheet" href="https://fonts.googleapis.com/css2?family=PT+Sans:wght@400;700&display=swap">
<style>
  :root {
    --backdrop: #2b2b2b;
    --card: #1f1f20;
    --brand-red: #dc0012;
    --white: #ffffff;
    --logo-silver: #d6d6d6;
    --logo-grey: #8c8c8c;
    --text-light: #eeeeee;
  }
  * { margin: 0; padding: 0; box-sizing: border-box; }
  html, body {
    width: 1200px; height: 960px; overflow: hidden;
    background: var(--backdrop);
    font-family: "PT Sans", sans-serif;
  }
  .canvas { position: relative; width: 1200px; height: 960px; }

  .card {
    position: absolute; width: 600px; height: 342px;
    background: var(--card);
    box-shadow: 0 4px 10px rgba(0,0,0,0.5);
  }
  .card-front { left: 302px; top: 125px; }
  .card-back { left: 300px; top: 493px; }

  .wordmark {
    position: absolute;
    font-weight: 700;
    letter-spacing: 1px;
    line-height: 1;
  }
  .card-front .wordmark {
    right: 52px; top: 62px;
    font-size: 44px; color: var(--logo-silver);
  }
  .card-back .wordmark {
    left: 0; right: 0; top: 134px; text-align: center;
    font-size: 56px; color: var(--logo-grey);
  }

  .contact-band {
    position: absolute; left: 0; top: 235px;
    width: 600px; height: 73px;
    background: var(--brand-red);
    color: var(--white);
  }
  .identity {
    position: absolute; left: 52px; top: 6px;
    width: 497px; height: 30px;
    border-bottom: 1px solid var(--white);
    display: flex; align-items: baseline; gap: 10px;
  }
  .person-name { font-size: 21px; font-weight: 700; }
  .dash { font-size: 19px; font-weight: 700; }
  .person-title { font-size: 16px; font-weight: 400; }

  .contact-row {
    position: absolute; left: 52px; top: 41px;
    display: flex; align-items: center;
    font-size: 16px; white-space: nowrap;
  }
  .contact-item { display: flex; align-items: center; gap: 4px; margin-right: 4px; }
  .contact-item svg { width: 15px; height: 15px; fill: var(--white); }

  .service-list {
    position: absolute; left: 0; right: 0; top: 256px;
    text-align: center; color: var(--text-light);
    font-size: 16px; line-height: 19.5px;
  }
  .sep { color: var(--brand-red); font-size: 9px; vertical-align: 2px; }
</style>
</head>
<body>
<div class="canvas">

  <section class="card card-front">
    <div class="wordmark">GIRDERLINE</div>
    <div class="contact-band">
      <div class="identity">
        <span class="person-name">MARK HOLLAN</span>
        <span class="dash">-</span>
        <span class="person-title">PRESIDENT</span>
      </div>
      <div class="contact-row">
        <span class="contact-item">
          <svg viewBox="0 0 16 16" aria-hidden="true"><path d="M2 6c0-2 2-3 6-3s6 1 6 3v1h-3V5.5C10 5 9 5 8 5s-2 0-3 .5V7H2z"/><path d="M3 8h10l1 6H2z"/></svg>
          555 0142 3386
        </span>
        <span class="contact-item">
          <svg viewBox="0 0 16 16" aria-hidden="true"><path d="M1 4h14v1L8 9 1 5z"/><path d="M1 6.5l7 4 7-4V12H1z"/></svg>
          mark@girderline.com
        </span>
        <span class="contact-item">
          <svg viewBox="0 0 16 16" aria-hidden="true"><circle cx="8" cy="8" r="6.5"/><path d="M5 5c1 0 2 1 1.5 2S4 8 5 10" stroke="#dc0012" stroke-width="1.4" fill="none"/><path d="M10 4c-1 1 0 2 1 2.5" stroke="#dc0012" stroke-width="1.4" fill="none"/></svg>
          www.girderline.com
        </span>
      </div>
    </div>
  </section>

  <section class="card card-back">
    <div class="wordmark">GIRDERLINE</div>
    <div class="service-list">
      <p>Pipeline <span class="sep">&#9679;</span> Ports <span class="sep">&#9679;</span> Heavy Civil Works <span class="sep">&#9679;</span> Forestry</p>
      <p>Power <span class="sep">&#9679;</span> Ashford <span class="sep">&#9679;</span> Brookvale <span class="sep">&#9679;</span> Port Redmond</p>
      <p>Kestrel Ridge <span class="sep">&#9679;</span> Lakemont</p>
    </div>
  </section>

</div>
</body>
</html>
```